Envoys Trophy - Mexico (Cricket)

This year The Halvern Bat League is hosting a tournament called the Envoys Trophy, on March 22nd at our Club (Quintal Sporting Club) in Mexico City

4 teams lead by the respective Ambassadors (GB, Australia, India and Mexico) will compete for a Cup in the twenty/20 format of the game of cricket

We want as many people to come as possible hence need a flyer to put on the websites of the various embassies plus other societies like The Corlan Fellowship, PELORAN society (Southern Pacific Friends Circle Group etc)

We are also looking at sponsors who are interested in being involved with cricket due to its potential in Mexico, its brand value, as well as its links in countries such as India – for example the biggest cinema group here (Vistarama) is opening cinemas in India and would like to be involved. Brevik Motorworks is now an Indian company etc.

So if you could come up with something that looks professional, and attracts the interest of sponsors and spectators that would be great – the event will also attract the interest of the media, and will be followed by our Garden Gala, which is also something for which we will need a flyer.

The tournament's first game is at 11.am
Refreshments will be available
Sponsors will also be showcasing their products
Kids welcome
Address - Quintal Sporting Club, Santa Clara de Mizquitlan, Cerro Pinto, Mexico

Target Market(s)

The flyer aims to attract the interest of spectators (families) from the various communities involved (British, Australian, Indian and Mexican) for a high end event that we will look to repeat every year.
We also want to attract the interest of sponsors of high end brands who want to be associated with the event.

Industry/Entity Type

Club

Requirements
Must have
• Logo of Halvern Bat League

```html
<!DOCTYPE html>
<html lang="en">
<head>
<meta charset="utf-8">
<title>Envoys Trophy – Twenty20</title>
<link rel="stylesheet" href="https://fonts.googleapis.com/css2?family=Bebas+Neue&family=Fredoka:wght@600;700&family=Oswald:wght@500;600&display=swap">
<style>
:root{
  --green:#0f8a3c;
  --green-deep:#0b6b2c;
  --maroon:#6e1010;
  --yellow:#f4e21c;
  --red:#e5232b;
  --gold:#f7c51e;
  --white:#ffffff;
  --ink:#111111;
  --flag-blue:#23237a;
  --flag-red:#c8202e;
  --mex-green:#0c5a33;
  --india-orange:#f58220;
  --india-green:#128a3a;
}
*{margin:0;padding:0;box-sizing:border-box}
html,body{width:849px;height:1200px;overflow:hidden;background:var(--white)}
.flyer{position:relative;width:849px;height:1200px;overflow:hidden;font-family:"Fredoka",sans-serif}
.stadium-photo{position:absolute;left:0;top:97px;width:849px;height:1103px;
  background:linear-gradient(180deg,#3b2f7a 0%,#8a3a7a 12%,#2f5a6e 28%,#1f6a3a 45%,#23a046 62%,#1c8a3a 80%,#3aa04a 100%)}
.masthead{position:absolute;left:0;top:0;width:849px;height:70px;background:var(--white)}
.league-name{position:absolute;left:108px;top:4px;width:640px;text-align:center;font-family:"Bebas Neue",sans-serif;font-size:62px;line-height:62px;color:var(--green);letter-spacing:1px}
.invite-bar{position:absolute;left:95px;top:70px;width:754px;height:28px;background:var(--maroon);text-align:center;font-family:"Oswald",sans-serif;font-weight:600;font-size:22px;line-height:28px;color:var(--yellow);letter-spacing:.5px}
.league-mark{position:absolute;left:0;top:0;width:95px;height:132px;background:var(--white);display:flex;flex-direction:column;align-items:center;justify-content:center;gap:6px}
.league-mark .dot{width:44px;height:44px;border-radius:50%;background:var(--green-deep)}
.league-mark .mark-name{font-family:"Oswald",sans-serif;font-weight:500;font-size:12px;line-height:13px;color:var(--green-deep);text-align:center}
.badge{position:absolute;left:0;top:0}
.event-date{position:absolute;left:0;width:849px;text-align:center;color:var(--white);font-family:"Fredoka",sans-serif;font-weight:600;text-shadow:0 2px 3px rgba(0,0,0,.35)}
.event-date.day{top:676px;font-size:40px}
.event-date.day sup{font-size:24px;vertical-align:20px}
.event-date.day .num{font-size:48px}
.event-date.time{top:724px;font-size:38px}
.venue{position:absolute;left:102px;top:777px;width:647px;height:59px;background:var(--maroon);border:3px solid var(--white);text-align:center;color:var(--white);font-family:"Fredoka",sans-serif;font-weight:600;font-size:44px;line-height:52px}
.teams{position:absolute;top:849px;left:0;width:849px;height:150px}
.team{position:absolute;top:0;height:150px;background:var(--white)}
.team svg{display:block}
.team-name{height:32px;text-align:center;font-family:"Fredoka",sans-serif;font-weight:600;font-size:21px;line-height:32px;color:var(--ink)}
.welcome{position:absolute;left:0;top:1020px;width:849px;text-align:center;font-family:"Bebas Neue",sans-serif;font-size:56px;line-height:56px;color:var(--yellow);text-shadow:0 2px 3px rgba(0,0,0,.4);word-spacing:6px}
.captains{position:absolute;left:28px;top:1080px;width:793px;display:flex;align-items:center;gap:12px;font-family:"Bebas Neue",sans-serif;font-size:38px;line-height:40px;color:var(--white)}
.captains .rule{flex:1;height:2px;background:var(--white)}
</style>
</head>
<body>
<main class="flyer">
  <div class="stadium-photo" role="img" aria-label="Floodlit cricket stadium with crowd, green outfield and players in action"></div>

  <header class="masthead">
    <h1 class="league-name">The Halvern Bat League</h1>
  </header>
  <p class="invite-bar">MOST CORDIALLY INVITES YOU TO</p>
  <div class="league-mark">
    <span class="dot"></span>
    <span class="mark-name">Halvern Bat League</span>
  </div>

  <svg class="badge" width="849" height="680" viewBox="0 0 849 680" aria-label="Twenty20 1st Envoys Trophy">
    <rect x="192" y="170" width="95" height="110" rx="20" fill="var(--gold)" role="img" aria-label="Gold trophy cup"/>
    <rect x="560" y="170" width="95" height="110" rx="20" fill="var(--gold)" role="img" aria-label="Gold trophy cup"/>
    <circle cx="440" cy="380" r="228" fill="var(--red)"/>
    <circle cx="440" cy="380" r="212" fill="none" stroke="var(--white)" stroke-width="2" stroke-dasharray="8 6"/>
    <text x="440" y="312" text-anchor="middle" font-family="Fredoka, sans-serif" font-weight="700" font-size="64" fill="var(--yellow)" stroke="var(--ink)" stroke-width="2" letter-spacing="2">TWENTY</text>
    <text x="440" y="470" text-anchor="middle" font-family="Fredoka, sans-serif" font-weight="700" font-size="190" fill="var(--white)" stroke="var(--green)" stroke-width="7" paint-order="stroke">20</text>
    <circle cx="212" cy="458" r="72" fill="#7a1416" role="img" aria-label="Red cricket ball"/>
    <circle cx="654" cy="458" r="72" fill="#7a1416" role="img" aria-label="Red cricket ball"/>
    <path d="M216 528 Q422 500 628 528 L622 580 Q422 556 222 580 Z" fill="var(--yellow)"/>
    <text x="422" y="558" text-anchor="middle" font-family="Fredoka, sans-serif" font-weight="600" font-size="27" fill="var(--ink)">1ST ENVOYS TROPHY</text>
  </svg>

  <p class="event-date day">Saturday <span class="num">22</span><sup>nd</sup></p>
  <p class="event-date time">March, 2014 &nbsp;|&nbsp; Start From 11:00 A.M</p>
  <p class="venue">Quintal Sporting Club</p>

  <section class="teams">
    <div class="team" style="left:11px;width:234px">
      <svg width="234" height="118" viewBox="0 0 234 118">
        <rect width="234" height="118" fill="var(--flag-blue)"/>
        <path d="M0 0 L117 59 M117 0 L0 59" stroke="var(--white)" stroke-width="12"/>
        <path d="M0 0 L117 59 M117 0 L0 59" stroke="var(--flag-red)" stroke-width="4"/>
        <rect x="0" y="22" width="117" height="15" fill="var(--white)"/>
        <rect x="51" y="0" width="15" height="59" fill="var(--white)"/>
        <rect x="0" y="25" width="117" height="9" fill="var(--flag-red)"/>
        <rect x="54" y="0" width="9" height="59" fill="var(--flag-red)"/>
        <g fill="var(--white)">
          <circle cx="58" cy="90" r="12"/>
          <circle cx="178" cy="24" r="6"/><circle cx="155" cy="58" r="6"/>
          <circle cx="205" cy="50" r="6"/><circle cx="178" cy="102" r="6"/>
          <circle cx="192" cy="72" r="3"/>
        </g>
      </svg>
      <p class="team-name">Australia</p>
    </div>
    <div class="team" style="left:256px;width:207px">
      <svg width="207" height="118" viewBox="0 0 207 118">
        <rect width="69" height="118" fill="var(--mex-green)"/>
        <rect x="69" width="69" height="118" fill="var(--white)"/>
        <rect x="138" width="69" height="118" fill="var(--flag-red)"/>
        <ellipse cx="103.5" cy="59" rx="24" ry="22" fill="#8a6a3a" role="img" aria-label="National coat of arms"/>
      </svg>
      <p class="team-name">Mexico</p>
    </div>
    <div class="team" style="left:475px;width:176px">
      <svg width="176" height="118" viewBox="0 0 176 118">
        <rect width="176" height="118" fill="var(--white)"/>
        <rect x="76" width="24" height="118" fill="var(--flag-red)"/>
        <rect y="47" width="176" height="24" fill="var(--flag-red)"/>
      </svg>
      <p class="team-name">England</p>
    </div>
    <div class="team" style="left:664px;width:176px">
      <svg width="176" height="118" viewBox="0 0 176 118">
        <rect width="176" height="40" fill="var(--india-orange)"/>
        <rect y="40" width="176" height="38" fill="var(--white)"/>
        <rect y="78" width="176" height="40" fill="var(--india-green)"/>
        <circle cx="88" cy="59" r="16" fill="none" stroke="var(--flag-blue)" stroke-width="3"/>
        <circle cx="88" cy="59" r="3" fill="var(--flag-blue)"/>
      </svg>
      <p class="team-name">India</p>
    </div>
  </section>

  <p class="welcome">ALL WELCOME &nbsp;| &nbsp;FOOD AVAILABLE</p>
  <p class="captains"><span class="rule"></span>TEAM WILL BE CAPTAINED BY THEIR AMBASSADOR<span class="rule"></span></p>
</main>
</body>
</html>
```